Financial planning organization needs an PLVK postcard inviting 55+ community to attend a monthly...

We need a standard postcard to use for our monthly tea and financial discussion at a senior living community. The tea features an informal discussion with a Licensed Money Counselor to address the news of the day as well as personal financial questions. We would like to see designs that use graphics rather than photos. In earlier attempts we found the photos of people just not working. Final design should be clean and simple.

Target Market(s)

55+ Community (senior citizens)

Industry/Entity Type

Financial Planning

Font styles to use
Serif
Sans Serif

Requirements
Must have
• PLVK formatting
• Graphics/ graphic heavy

```html
<!DOCTYPE html>
<html lang="en">
<head>
<meta charset="UTF-8">
<title>Tea with Ned – Hallworth Advisors</title>
<link rel="stylesheet" href="https://fonts.googleapis.com/css2?family=Old+Standard+TT:ital,wght@0,400;0,700;1,400&family=Didact+Gothic&display=swap">
<style>
  :root {
    --ink: #111111;
    --panel: rgba(250, 248, 249, 0.9);
    --bg-dark: #4a3c38;
    --bg-mid: #8a7068;
    --bg-light: #d9cfcc;
    --portrait: #7b6f66;
  }
  * { margin: 0; padding: 0; box-sizing: border-box; }
  html, body { width: 1200px; height: 1200px; overflow: hidden; background: var(--bg-dark); }
  .postcard { position: relative; width: 1200px; height: 1200px; overflow: hidden; }

  .backdrop {
    position: absolute; inset: 0;
    background:
      radial-gradient(circle at 12% 20%, #c9a27a 0, rgba(201,162,122,0) 22%),
      radial-gradient(circle at 60% 45%, var(--bg-light) 0, rgba(217,207,204,0) 55%),
      linear-gradient(160deg, var(--bg-mid) 0%, var(--bg-dark) 100%);
  }

  .panel {
    position: absolute; left: 19px; top: 68px; width: 1161px; height: 1062px;
    background: var(--panel);
  }

  .portrait {
    position: absolute; left: 172px; top: 241px; width: 248px; height: 248px;
    border-radius: 50%;
    background: linear-gradient(180deg, #a89588 0%, var(--portrait) 55%, #2e3140 100%);
  }

  .bio {
    position: absolute; left: 32px; top: 523px; width: 600px;
    font-family: "Old Standard TT", serif; font-style: italic; font-weight: 400;
    font-size: 28.5px; line-height: 38px; letter-spacing: 1.2px; color: var(--ink);
  }
  .bio .lead { display: block; padding-left: 168px; }

  .title {
    font-family: "Old Standard TT", serif; font-weight: 400; color: var(--ink);
  }
  .title .word {
    position: absolute; left: 680px; display: block;
    font-size: 140px; line-height: 1; letter-spacing: 7px; font-weight: 400;
  }
  .title .word-tea { top: 232px; }
  .title .word-with { top: 403px; left: 686px; letter-spacing: 9px; }
  .title .word-name { top: 574px; left: 690px; font-style: italic; letter-spacing: 10px; }

  .rule { position: absolute; left: 671px; height: 5px; background: var(--ink); }
  .rule-1 { top: 374px; width: 332px; }
  .rule-2 { top: 546px; width: 453px; }
  .rule-3 { top: 718px; width: 344px; }

  .details {
    position: absolute; left: 604px; top: 772px;
    font-family: "Didact Gothic", sans-serif; color: var(--ink);
  }
  .details .when { font-size: 35px; line-height: 44px; display: block; }
  .details .fare {
    margin-top: 26px; font-size: 25.5px; line-height: 38px; font-style: italic; display: block;
  }

  .tea-art-tier {
    position: absolute; left: 786px; top: 985px; width: 96px; height: 96px; border-radius: 12px;
    background: linear-gradient(180deg, #e9d8c8 0%, #d7a99a 60%, #c89b6a 100%);
  }
  .tea-art-pot {
    position: absolute; left: 897px; top: 1000px; width: 96px; height: 68px; border-radius: 12px;
    background: linear-gradient(180deg, #f1f0ee 0%, #d8d6d2 100%);
  }

  .brand {
    position: absolute; left: 32px; top: 1072px; display: flex; align-items: center; gap: 12px;
    color: var(--ink); font-family: "Didact Gothic", sans-serif; font-weight: 400;
  }
  .brand .dot { width: 22px; height: 22px; border-radius: 50%; background: var(--ink); }
  .brand .name { font-size: 30px; line-height: 1; }
</style>
</head>
<body>
<main class="postcard">
  <div class="backdrop" role="img" aria-label="Softly blurred tea table with teapot, cups, biscuits and a dotted napkin"></div>
  <section class="panel"></section>

  <div class="portrait" role="img" aria-label="Portrait of the money counselor in a circular frame"></div>

  <p class="bio">
    <span class="lead">Ned Hallworth is a</span>
    LICENSED MONEY COUNSELOR<br>
    and Fiduciary specializing in asset<br>
    management of IRA, retirement,<br>
    investment, and trust accounts.<br>
    Hallworth Advisors, LLC is an<br>
    independent Registered Investment<br>
    Advisor with a low cost,<br>
    commission-free business model.
  </p>

  <h1 class="title">
    <span class="word word-tea">TEA</span>
    <span class="word word-with">WITH</span>
    <span class="word word-name">NED</span>
  </h1>
  <div class="rule rule-1"></div>
  <div class="rule rule-2"></div>
  <div class="rule rule-3"></div>

  <div class="details">
    <span class="when">Thursday, August 15th at 3:00pm</span>
    <span class="when">Maple Court Hall</span>
    <span class="fare">Tea, lemonade and sweets<br>will be served discussion and open forum.</span>
  </div>

  <div class="tea-art-tier" role="img" aria-label="Illustration of a tiered stand of cakes with a teapot and cup"></div>
  <div class="tea-art-pot" role="img" aria-label="Illustration of a white teapot and a cup of tea"></div>

  <div class="brand">
    <span class="dot"></span>
    <span class="name">Hallworth Advisors</span>
  </div>
</main>
</body>
</html>
```